Halvorsen Partners Business Card

Halvorsen Partners Civil Construction
Marcus Halvorsen
CEO
727-518-6094
Marcus@HalvorsenSiteworks.example
www.HalvorsenSiteworks.example
Site Development
Utility Construction
Excavation
40876 County Lane 19
Land O' Lakes, FL 34638

Target Market(s)

Construction and government

Industry/Entity Type

Business

Contact Information for Business Card

I want an unique design that make a statement

Number of Pages Required

1 page

Font styles to use

Colors

Designer to choose colors to be used in the design.

Requirements
Must have
• unique design, feel free to modify or change the color of my logo.
Nice to have
• extra design features like spot UV, foil accents, color edges, unique paper, or any thing that would make my card pop.
• I like the feel of the image that I attached

```html
<!DOCTYPE html>
<html lang="en">
<head>
<meta charset="utf-8">
<title>Halvorsen Partners Business Card</title>
<link href="https://fonts.googleapis.com/css2?family=Josefin+Sans:wght@400;600;700&display=swap" rel="stylesheet">
<style>
  :root {
    --backdrop: #dfe6e8;
    --night-blue: #2f3f80;
    --ink: #0b0b0d;
    --paper: #ffffff;
    --accent: #6a7dd6;
    --shadow: rgba(20, 30, 40, 0.28);
  }
  * { margin: 0; padding: 0; box-sizing: border-box; }
  html, body {
    width: 1200px;
    height: 600px;
    overflow: hidden;
    background: var(--backdrop);
    font-family: "Josefin Sans", sans-serif;
  }
  .canvas {
    position: relative;
    width: 1200px;
    height: 600px;
  }
  .card {
    position: absolute;
    top: 130px;
    width: 510px;
    height: 340px;
    background: var(--paper);
    overflow: hidden;
    box-shadow: 0 12px 30px var(--shadow);
  }
  .card--front { left: 60px; }
  .card--back { left: 630px; }
  .card__art {
    position: absolute;
    inset: 0;
    width: 510px;
    height: 340px;
  }
  .brand {
    position: absolute;
    display: flex;
    align-items: center;
    gap: 14px;
    color: var(--accent);
    font-weight: 600;
    text-transform: uppercase;
  }
  .brand__square {
    width: 44px;
    height: 44px;
    background: var(--accent);
    flex: none;
  }
  .brand__name {
    font-size: 22px;
    line-height: 1.15;
    letter-spacing: 0.5px;
  }
  .brand__name span { display: block; font-size: 15px; letter-spacing: 2.6px; }
  .card--front .brand { left: 92px; top: 146px; }
  .card--back .brand { left: 92px; top: 22px; }

  .contact {
    position: absolute;
    left: 0;
    right: 0;
    top: 226px;
    text-align: center;
    color: var(--ink);
    font-weight: 600;
    letter-spacing: 2px;
  }
  .contact__name { font-size: 14px; letter-spacing: 3.5px; text-transform: uppercase; }
  .contact__role { font-size: 11px; margin-top: 5px; }
  .contact__phone { font-size: 12px; margin-top: 5px; }
  .contact__email { font-size: 11px; margin-top: 5px; letter-spacing: 1.6px; }

  .services {
    position: absolute;
    left: 86px;
    top: 110px;
    list-style: none;
    color: var(--ink);
    font-weight: 700;
    font-size: 12.5px;
    letter-spacing: 2px;
    line-height: 17px;
  }
  .services li::before {
    content: "";
    display: inline-block;
    width: 8px;
    height: 8px;
    border-radius: 50%;
    background: var(--ink);
    margin-right: 6px;
    vertical-align: 1px;
  }
  .address {
    position: absolute;
    left: 86px;
    top: 172px;
    font-style: normal;
    color: var(--ink);
    font-size: 12px;
    line-height: 16px;
    letter-spacing: 0.4px;
  }
  .website {
    position: absolute;
    left: 86px;
    top: 212px;
    color: var(--ink);
    font-weight: 700;
    font-size: 11.5px;
    letter-spacing: 1.8px;
  }
</style>
</head>
<body>
<main class="canvas">

  <section class="card card--front" aria-label="Business card front">
    <svg class="card__art" viewBox="0 0 510 340">
      <defs>
        <linearGradient id="machinesFront" x1="0" y1="1" x2="0" y2="0">
          <stop offset="0" stop-color="#0b0b0d" stop-opacity="0.9"/>
          <stop offset="1" stop-color="#0b0b0d" stop-opacity="0.15"/>
        </linearGradient>
      </defs>
      <rect class="sky" width="510" height="150" fill="var(--night-blue)"/>
      <rect role="img" aria-label="Silhouettes of an excavator, dozer and dump truck on the job site" x="110" y="30" width="330" height="100" fill="url(#machinesFront)"/>
      <path class="ground-band" fill="var(--ink)"
        d="M0 128 L14 124 L28 126 L40 120 L58 125 L76 121 L96 126 L120 124 L150 127 L180 122 L210 125 L240 121 L270 124 L300 120 L330 123 L360 119 L390 123 L420 118 L450 122 L480 116 L510 118
           L510 208 L496 211 L482 207 L466 212 L450 209 L430 213 L410 208 L392 212 L372 209 L350 213 L330 208 L310 211 L290 207 L270 212 L250 209 L230 213 L210 208 L190 212 L170 209 L150 213 L130 208 L110 211 L90 207 L70 212 L50 208 L30 212 L14 209 L0 212 Z"/>
      <path class="base-band" fill="var(--ink)"
        d="M0 312 L18 309 L36 313 L56 308 L78 312 L100 309 L124 313 L148 308 L172 312 L196 309 L222 313 L248 308 L274 312 L300 309 L326 313 L352 308 L378 312 L404 309 L430 313 L456 308 L482 312 L510 309 L510 340 L0 340 Z"/>
    </svg>
    <div class="brand">
      <div class="brand__square"></div>
      <div class="brand__name">Halvorsen Partners<span>Civil Construction</span></div>
    </div>
    <div class="contact">
      <div class="contact__name">Marcus Halvorsen</div>
      <div class="contact__role">CEO</div>
      <div class="contact__phone">727-518-6094</div>
      <div class="contact__email">Marcus@HalvorsenSiteworks.example</div>
    </div>
  </section>

  <section class="card card--back" aria-label="Business card back">
    <svg class="card__art" viewBox="0 0 510 340">
      <defs>
        <linearGradient id="machinesBack" x1="0" y1="1" x2="0" y2="0">
          <stop offset="0" stop-color="#0b0b0d" stop-opacity="0.85"/>
          <stop offset="1" stop-color="#0b0b0d" stop-opacity="0.1"/>
        </linearGradient>
      </defs>
      <path class="header-band" fill="var(--ink)"
        d="M0 0 L510 0 L510 92 L494 95 L476 90 L458 96 L440 92 L420 97 L400 91 L380 95 L360 90 L340 96 L320 92 L300 97 L280 91 L260 95 L240 90 L220 96 L200 92 L180 97 L160 91 L140 95 L120 90 L100 96 L80 92 L60 97 L40 91 L20 95 L0 92 Z"/>
      <g role="img" aria-label="Silhouettes of an excavator, dozer and dump truck on the job site">
        <rect x="290" y="214" width="160" height="80" fill="url(#machinesBack)"/>
        <rect x="112" y="256" width="178" height="38" fill="url(#machinesBack)"/>
      </g>
      <path class="ground-band" fill="var(--ink)"
        d="M0 300 L14 296 L30 299 L46 293 L64 297 L84 294 L110 298 L140 295 L170 299 L200 294 L230 297 L260 293 L290 297 L320 292 L350 296 L380 292 L410 295 L440 290 L470 294 L510 291 L510 340 L0 340 Z"/>
    </svg>
    <div class="brand">
      <div class="brand__square"></div>
      <div class="brand__name">Halvorsen Partners<span>Civil Construction</span></div>
    </div>
    <ul class="services">
      <li>Site Development</li>
      <li>Utility Construction</li>
      <li>Excavation</li>
    </ul>
    <address class="address">40876 County Lane 19<br>Land O' Lakes, FL 34638</address>
    <div class="website">www.HalvorsenSiteworks.example</div>
  </section>

</main>
</body>
</html>
```